Broschüren-Design für gemeinnützige Organisation
Zielgruppe
Als gemeinnützige Organisation unterstützen wir Kinder und Jugendliche, vor allem in den Bereichen Schul- und Berufsausbildung. Wir arbeiten vorwiegend in Ostafrika, vor allem in Tansania und Kenia. Mit dieser Broschüre wollen wir für unser neues Pilotprojekt werben, den Aufbau eines dualen Ausbildungszentrums für junge Menschen in Kenia. Ziel des Ausbildungszentrums ist es jungen Menschen eine qualifizierte Berufsausbildung zu ermöglichen und damit Perspektiven und Zukunft im Heimatland.
Unsere Zielgruppe: Menschen mit Herz und Weitblick von 18 bis 80+
Aufgabenstellung
Die Broschüre sollte handlich sein und leicht zum einstecken. Derzeit haben wir den Text und die Gestaltung auf das Format DIN lang hoch (105x210 mm, 12 Seiten) ausgelegt. Ist aber nur ein Vorschlag und kein muss.
Die einzige Vorgabe ist das orange aus dem Logo mit der Farbe #ff3300 Ansonsten gibt es keine Vorgaben was Schrift, Farbgestaltung, Layout, Form, Seitenanzahl...ect betrifft. Allerdings sollte darauf geachtet werden, dass die Textinhalte der Doppelseiten erhalten bleiben (z.B. Seite 2 links - Seite 3 rechts, usw.)
Mitgeliefert werden Fotos, die gerne Verwendung finden können. Sollten aber weitere oder aussagekräftigere Fotos und Hintergründe benötigt werden, sind wir absolut offen dafür.

```html
<!DOCTYPE html>
<html lang="de">
<head>
<meta charset="utf-8">
<title>Broschüre – Duales Ausbildungszentrum</title>
<link href="https://fonts.googleapis.com/css2?family=Roboto+Condensed:ital,wght@0,700;1,700&family=Cabin:wght@400;600&display=swap" rel="stylesheet">
<style>
  :root {
    --orange: #ff3300;
    --navy: #2b2a8f;
    --ink: #1f1f1f;
    --grey-quote: #3a3a3a;
    --paper: #ffffff;
    --backdrop: #e4e4e8;
    --fold: rgba(0,0,0,0.08);
  }
  * { box-sizing: border-box; margin: 0; padding: 0; }
  html, body { width: 728px; height: 1200px; overflow: hidden; }
  body {
    background: var(--backdrop);
    font-family: "Cabin", sans-serif;
    color: var(--ink);
    position: relative;
  }
  .spread {
    position: absolute;
    left: 24px;
    width: 680px;
    height: 510px;
    display: flex;
    box-shadow: 0 6px 18px rgba(0,0,0,0.15);
  }
  .spread--details { top: 50px; }
  .spread--support { top: 600px; }
  .page {
    width: 340px;
    height: 100%;
    background: var(--paper);
    padding: 0 26px 24px;
    position: relative;
  }
  .page--left { background: linear-gradient(to left, var(--fold), transparent 18px), var(--paper); }
  .page--right { background: linear-gradient(to right, var(--fold), transparent 18px), var(--paper); }
  .section-tag {
    display: inline-block;
    background: var(--navy);
    color: #fff;
    font-family: "Roboto Condensed", sans-serif;
    font-weight: 700;
    font-size: 8.5px;
    letter-spacing: 0.3px;
    text-transform: uppercase;
    padding: 4px 10px;
    margin-top: 22px;
  }
  .heading {
    font-family: "Roboto Condensed", sans-serif;
    font-weight: 700;
    color: var(--orange);
    font-size: 17px;
    line-height: 1.1;
    margin: 12px 0 5px;
  }
  .heading--caps { text-transform: uppercase; font-size: 17px; margin-top: 40px; }
  .body-text {
    font-size: 8.4px;
    line-height: 1.42;
  }
  .photo {
    margin: 14px 0 6px;
    height: 170px;
    background: linear-gradient(135deg, #d9d3dc 0%, #9c8f95 35%, #3b2e2c 60%, #c9bfc4 100%);
  }
  .page--goals { padding-top: 82px; }
  .pull-quote { margin-top: 30px; position: relative; }
  .pull-quote__rule {
    display: flex; align-items: center; gap: 6px;
    color: var(--orange);
    font-family: "Roboto Condensed", sans-serif;
    font-weight: 700; font-size: 22px; line-height: 1;
  }
  .pull-quote__rule::before, .pull-quote__rule::after {
    content: ""; height: 1px; background: var(--orange); flex: 1;
  }
  .pull-quote__rule--top::before { flex: 0 0 26px; }
  .pull-quote__rule--bottom::after { flex: 0 0 26px; }
  .pull-quote__text {
    font-family: "Roboto Condensed", sans-serif;
    font-style: italic; font-weight: 700;
    color: var(--grey-quote);
    font-size: 14.5px; line-height: 1.25;
    padding: 6px 4px 8px;
  }
  .membership { display: flex; gap: 10px; margin-top: 16px; }
  .membership__tier { flex: 1; }
  .membership__card { height: 54px; border-radius: 4px; }
  .membership__card--ivory { background: linear-gradient(135deg, #f3c6c8, #6f5a60 50%, #e6b8bb); }
  .membership__card--silver { background: linear-gradient(135deg, #cfe5ee, #5f7f8f 50%, #d4e8f0); }
  .membership__card--gold { background: linear-gradient(135deg, #f0d98a, #9c7a26 50%, #ead07a); }
  .membership__name {
    font-family: "Cabin", sans-serif; font-weight: 600;
    font-size: 9px; letter-spacing: 0.3px; margin-top: 6px; text-transform: uppercase;
  }
  .membership__range { font-size: 7px; margin-bottom: 5px; }
  .membership__benefit { font-size: 6.8px; line-height: 1.35; }
  .wall-of-fame {
    margin-top: 6px; height: 140px;
    background: linear-gradient(120deg, #e8c52a, #2fb6b0 25%, #c6273a 50%, #3a63c9 75%, #f2a21a);
  }
  .wall-caption { margin-top: 8px; }
</style>
</head>
<body>

<section class="spread spread--details">
  <article class="page page--left">
    <span class="section-tag">Details zum Ausbildungszentrum</span>
    <h2 class="heading">Berufsschule</h2>
    <p class="body-text">Um möglichst schnell mit der Berufsausbildung junger Menschen beginnen zu können bauen wir die Berufsschule in zwei Phasen auf. Mit Fertigstellung der Phase 1 können pro Ausbildungszyklus 128 junge Menschen ausgebildet werden. Nach Abschluss der Bauphase 2 werden in jedem Ausbildungszyklus 256 junge Menschen eine qualifizierte Berufsausbildung erhalten.</p>
    <div class="photo" role="img" aria-label="Foto: zwei junge Auszubildende mit Schürzen in einer Lehrküche schauen gemeinsam auf ein Tablet"></div>
    <h2 class="heading">Der praktische Lehrbetrieb</h2>
    <p class="body-text">Als praktischer Lehrbetrieb wird ein kleines Hotel mit Lehrküche und Restaurant aufgebaut. Während der dreijährigen Ausbildungszeit lernen die jungen Menschen hier alles, was auf dem Arbeitsmarkt an praktischen Fähigkeiten, Können und Wissen verlangt wird. Nach Abschluss der Ausbildung werden sie sofort vom Arbeitsmarkt aufgenommen, der dringend hervorragend ausgebildete Fachkräfte benötigt.</p>
  </article>
  <article class="page page--right page--goals">
    <h2 class="heading">Zielsetzung der Ausbildung</h2>
    <p class="body-text">Ziel der Ausbildung ist der Erhalt eines Diploms. Zusammen mit den Prüfungsergebnissen gibt es Auskunft über die Qualifizierung, sowie die persönlichen Fähigkeiten und das Können der jungen Menschen. Außerdem soll es ihre nationale und internationale Wettbewerbsfähigkeit zum Ausdruck bringen.</p>
    <h2 class="heading">Selbstfinanzierung und Nachhaltigkeit</h2>
    <p class="body-text">Ein weiterer wichtiger Punkt, der durch den praktischen Lehrbetrieb erreicht wird, ist die Selbstfinanzierung und die daraus entstehende Nachhaltigkeit. Bereits 26 Zimmer im Lehrhotel reichen aus, um mittelfristig, nach Aufbau des dualen Ausbildungszentrums, die Selbstfinanzierung zu gewährleisten. Die Erträge aus Lehrhotel und Lehrküche machen es möglich, das komplette duale Ausbildungszentrum in der Zukunft selbst zu finanzieren, mit allen Lehrern, Fachpersonal und Lehrmaterial.</p>
    <blockquote class="pull-quote">
      <div class="pull-quote__rule pull-quote__rule--top">”</div>
      <p class="pull-quote__text">Hunderte junger Menschen können an nur einem Ausbildungsort eine qualifizierte Berufsausbildung erhalten, ohne weitere finanzielle Hilfestellung und Unterstützung von außen!</p>
      <div class="pull-quote__rule pull-quote__rule--bottom">“</div>
    </blockquote>
  </article>
</section>

<section class="spread spread--support">
  <article class="page page--left">
    <h2 class="heading heading--caps">Für den Aufbau brauchen<br>wir Ihre Unterstützung</h2>
    <p class="body-text">Das duale Ausbildungszentrum wird sich in der Zukunft selbst finanzieren können und hunderten von Jugendlichen eine qualifizierte Berufsausbildung und damit Zukunft in ihrer Heimat ermöglichen. Für den Aufbau brauchen wir Ihre Hilfe. Deshalb suchen wir Visionäre, Menschen mit Herz und Weitblick die zusammen mit uns das duale Ausbildungszentrum aufbauen wollen.</p>
    <h2 class="heading">Einzelspende</h2>
    <p class="body-text">Wir bedanken uns für jede Spende. Denn jede Spende macht einen Unterschied und ist herzlich willkommen!</p>
    <h2 class="heading">Als Projektpate den Aufbau begleiten</h2>
    <p class="body-text">Monatliche Spenden als Projektpate sind für uns besonders wichtig, damit wir langfristig planen können. Dabei ist die Höhe der monatlichen Spende nicht das Wichtigste. Wir wünschen uns, dass jeder mitmachen kann, der als Mensch mit Herz und Weitblick das Ausbildungszentrum zusammen mit uns aufbauen und begleiten möchte.</p>
    <h2 class="heading">Mitgliedskarte und Ermäßigung<br>als Gast im Lehrhotel</h2>
    <p class="body-text">Wir hoffen sehr, dass Sie als Projektpate das Lehrhotel im Ausbildungszentrum einmal besuchen kommen. Schließlich haben Sie es durch Ihre Spende gewissermaßen mit aufgebaut. Als Projektpate erhalten Sie eine lebenslang gültige Mitgliedskarte verbunden mit einer Ermäßigung als Gast im Lehrhotel.</p>
  </article>
  <article class="page page--right">
    <span class="section-tag">Unser Dankeschön für Ihre Hilfe</span>
    <div class="membership">
      <div class="membership__tier">
        <div class="membership__card membership__card--ivory" role="img" aria-label="Mitgliedskarte Ivory Member mit rosé-metallischem Strahlenmuster"></div>
        <p class="membership__name">Ivory Member</p>
        <p class="membership__range">monatl. Spende: 2 € bis 6 €</p>
        <p class="membership__benefit">Ihr Vorteil:<br>5% Ermäßigung auf den Zimmerpreis im Lehrhotel</p>
      </div>
      <div class="membership__tier">
        <div class="membership__card membership__card--silver" role="img" aria-label="Mitgliedskarte Silver Member mit silber-blauem Strahlenmuster"></div>
        <p class="membership__name">Silver Member</p>
        <p class="membership__range">monatl. Spende: 7 € bis 15 €</p>
        <p class="membership__benefit">Ihr Vorteil:<br>10% Ermäßigung auf den Zimmerpreis im Lehrhotel</p>
      </div>
      <div class="membership__tier">
        <div class="membership__card membership__card--gold" role="img" aria-label="Mitgliedskarte Gold Member mit goldenem Strahlenmuster"></div>
        <p class="membership__name">Gold Member</p>
        <p class="membership__range">monatl. Spende: 16 € und mehr</p>
        <p class="membership__benefit">Ihr Vorteil:<br>10% Ermäßigung auf den Zimmerpreis im Lehrhotel und auf sämtliche Speisen und Getränke aus der Gastronomie unseres Lehrbetriebs.</p>
      </div>
    </div>
    <h2 class="heading">Wall of Fame</h2>
    <div class="wall-of-fame" role="img" aria-label="Collage aus bunten Namensschildern der Spender für die Danke-Tafel"></div>
    <p class="body-text wall-caption">Auf dem Gelände des Ausbildungszentrums errichten wir eine große „Danke-Tafel“ in Form einer „Wall of Fame“. Jeder Spender und Projektpate wird dort namentlich erwähnt. Ihr Einverständnis natürlich vorausgesetzt.</p>
  </article>
</section>

</body>
</html>
```